K&M Trailer Rental promo Flyer 5.5x8.5" Flyer

All assets and several pictures of my trailers, that we rent out, are attached.

Flyer dimensions are 5.5"x8.5" - I'll be having it printed on glossy stock.
The dimensions and capacity of the trailers is key.
Include phone number: 248-555-0186 and our website kandmtrailer-example.com

I want something that will really "POP".

Target Market(s)

Blue collar business owners. Recreational offer roads/4x4 folks, used car dealers, contractors/small business owners. Folks with only occasional need for a trailer

Industry/Entity Type

Trailer Rental

Font styles to use
Other font styles liked:
• Designer's choice/no preference

Colors
EE7325
F08F49
F5BC92
FAE3D3
FDF4ED

Requirements
Must have
• Phone number, website, and details about our trailer offerings

```html
<!DOCTYPE html>
<html lang="en">
<head>
<meta charset="utf-8">
<title>K&amp;M Trailer Rental – Flyer</title>
<link href="https://fonts.googleapis.com/css2?family=Bebas+Neue&family=Poppins:wght@500;600;700;800&display=swap" rel="stylesheet">
<style>
  :root{
    --orange:#EE7325;
    --orange-soft:#F08F49;
    --peach:#F5BC92;
    --blush:#FAE3D3;
    --cream:#FDF4ED;
    --ink:#1f2a33;
    --muted:#6b6560;
    --white:#ffffff;
  }
  *{margin:0;padding:0;box-sizing:border-box}
  html,body{width:843px;height:1200px;overflow:hidden;background:var(--cream)}
  .flyer{position:relative;width:843px;height:1200px;overflow:hidden;background:var(--cream);font-family:"Poppins",sans-serif}
  .shapes{position:absolute;inset:0;width:843px;height:1200px}
  .brand{position:absolute;left:52px;top:128px;font-family:"Bebas Neue",sans-serif;font-size:37px;line-height:1;color:var(--ink);letter-spacing:.3px;display:flex;align-items:center;gap:10px}
  .brand-dot{width:14px;height:14px;border-radius:50%;background:var(--orange)}
  .headline{position:absolute;left:37px;top:472px;font-family:"Bebas Neue",sans-serif;font-size:56px;line-height:52px;color:var(--orange);letter-spacing:.5px}
  .rate-head,.rate-line,.rate-capacity{position:absolute;white-space:nowrap;transform:translateY(-50%)}
  .rate-head{font-weight:700;font-size:17px;color:var(--white);letter-spacing:.3px}
  .rate-line{font-size:19px}
  .rate-days{color:var(--muted);font-weight:500}
  .rate-price{color:var(--orange-soft);font-weight:600}
  .rate-capacity{left:376px;font-size:13.5px;font-weight:600;color:var(--ink)}
  .rate-capacity b{color:var(--orange);font-weight:700}
  .trailer-label{position:absolute;left:71px;width:234px;height:23px;display:flex;align-items:center;justify-content:center;color:var(--white);font-weight:700;font-size:13px;letter-spacing:.2px}
  .service-title{position:absolute;left:110px;top:1050px;font-family:"Bebas Neue",sans-serif;font-size:31px;line-height:1;color:var(--orange-soft)}
  .service-list{position:absolute;left:110px;top:1088px;display:grid;grid-template-columns:106px auto;row-gap:2px;font-size:12.5px;font-weight:600;color:var(--orange-soft);line-height:17px}
  .website{position:absolute;left:376px;width:440px;top:1046px;text-align:center;font-weight:700;font-size:20px;color:var(--orange);letter-spacing:.3px}
  .phone-number{position:absolute;left:494px;top:1122px;transform:translateY(-50%);font-weight:800;font-size:38px;color:var(--white);letter-spacing:.5px;white-space:nowrap}
</style>
</head>
<body>
<main class="flyer">
  <svg class="shapes" viewBox="80 60 893 1380" preserveAspectRatio="none">
    <defs>
      <linearGradient id="sky-yard" x1="0" y1="0" x2="0" y2="1">
        <stop offset="0" stop-color="#5d9be0"/>
        <stop offset=".45" stop-color="#8fb3c9"/>
        <stop offset=".7" stop-color="#4f6b3e"/>
        <stop offset="1" stop-color="#9b8a74"/>
      </linearGradient>
      <linearGradient id="rv-scene" x1="0" y1="0" x2="0" y2="1">
        <stop offset="0" stop-color="#7fb0dc"/>
        <stop offset=".55" stop-color="#c9c9c4"/>
        <stop offset="1" stop-color="#3a3c40"/>
      </linearGradient>
      <linearGradient id="lot-a" x1="0" y1="0" x2="1" y2="1">
        <stop offset="0" stop-color="#3d3f44"/>
        <stop offset=".5" stop-color="#b9b3a6"/>
        <stop offset="1" stop-color="#4a4c50"/>
      </linearGradient>
      <linearGradient id="lot-b" x1="0" y1="0" x2="1" y2="1">
        <stop offset="0" stop-color="#8d8f93"/>
        <stop offset=".5" stop-color="#c7a774"/>
        <stop offset="1" stop-color="#6f7175"/>
      </linearGradient>
    </defs>

    <rect class="band" x="80" y="820" width="893" height="37" fill="var(--orange-soft)"/>
    <rect class="band" x="80" y="1034" width="893" height="38" fill="var(--orange-soft)"/>
    <rect class="band" x="80" y="1310" width="893" height="80" fill="var(--orange-soft)"/>

    <rect class="side-panel" x="110" y="548" width="340" height="892" fill="var(--blush)"/>

    <g role="img" aria-label="Two classic cars loaded on a black tandem-axle flatbed trailer in front of a white house">
      <polygon points="488,60 973,60 973,435 655,435 600,513 120,513 262,288 375,288" fill="url(#sky-yard)"/>
    </g>
    <polygon class="accent-stripe" points="250,288 272,288 130,513 605,513 580,548 80,548 80,522" fill="var(--orange)"/>

    <g role="img" aria-label="Vintage motorhome loaded on a black flatbed trailer beside a white fence">
      <polygon points="655,450 973,450 973,727 510,727" fill="url(#rv-scene)"/>
    </g>
    <polygon class="accent-stripe" points="640,435 973,435 973,450 655,450 510,727 470,727" fill="var(--orange)"/>

    <rect x="110" y="805" width="340" height="183" fill="var(--orange)"/>
    <g role="img" aria-label="Black 20 by 7 foot car hauler trailer with wood deck in a parking lot">
      <rect x="118" y="818" width="322" height="167" fill="url(#lot-a)"/>
    </g>
    <rect x="155" y="960" width="248" height="27" fill="var(--orange)"/>

    <rect x="110" y="1022" width="340" height="183" fill="var(--orange)"/>
    <g role="img" aria-label="Black 20 by 7 foot car hauler trailer with tilt wood deck on pavement">
      <rect x="118" y="1033" width="322" height="170" fill="url(#lot-b)"/>
    </g>
    <rect x="155" y="1178" width="248" height="27" fill="var(--orange)"/>

    <g class="pin" fill="var(--orange-soft)">
      <path d="M160,1244 a22,22 0 0 1 22,22 c0,16 -22,38 -22,38 c0,0 -22,-22 -22,-38 a22,22 0 0 1 22,-22 z"/>
      <circle cx="160" cy="1266" r="9" fill="var(--blush)"/>
      <ellipse cx="160" cy="1308" rx="26" ry="4"/>
    </g>

    <rect x="497" y="1300" width="95" height="100" rx="16" fill="var(--orange-soft)" stroke="var(--white)" stroke-width="5"/>
    <rect x="506" y="1310" width="77" height="80" rx="10" fill="none" stroke="var(--white)" stroke-width="3"/>
    <path d="M526,1322 l12,-3 l9,22 l-9,7 c4,10 10,18 19,24 l7,-9 l21,10 l-3,12 c-30,2 -58,-30 -56,-63 z" fill="var(--white)"/>
  </svg>

  <div class="brand"><span class="brand-dot"></span>K&amp;M TRAILER RENTAL</div>

  <h1 class="headline">TRAILERS WE<br>HAVE AVAILABLE<br>TO OFFER YOU</h1>

  <section class="rates">
    <div class="rate-head" style="left:376px;top:681px">WEEK RATES</div>
    <div class="rate-head" style="left:623px;top:681px">WEEKEND RATES</div>
    <div class="rate-line rate-days" style="left:376px;top:716px">Monday to Thursday</div>
    <div class="rate-line rate-days" style="left:623px;top:716px">Friday to Sunday</div>
    <div class="rate-line rate-price" style="left:376px;top:749px">$85/Day*</div>
    <div class="rate-line rate-price" style="left:623px;top:749px">$85/Day*</div>
    <div class="rate-line rate-price" style="left:376px;top:782px">$350/Week*</div>
    <div class="rate-line rate-price" style="left:623px;top:782px">$200/Weekend*</div>
    <div class="rate-capacity" style="top:815px"><b>Capacity:</b> 7,000 lb GVWR · 20' x 7' deck · 2 axles</div>

    <div class="rate-head" style="left:383px;top:866px">WEEK RATES</div>
    <div class="rate-head" style="left:630px;top:866px">WEEKEND RATES</div>
    <div class="rate-line rate-days" style="left:376px;top:904px">Monday to Thursday</div>
    <div class="rate-line rate-days" style="left:630px;top:904px">Friday to Sunday</div>
    <div class="rate-line rate-price" style="left:376px;top:937px">$85/Day*</div>
    <div class="rate-line rate-price" style="left:630px;top:937px">$85/Day*</div>
    <div class="rate-line rate-price" style="left:376px;top:970px">$350/Week*</div>
    <div class="rate-line rate-price" style="left:630px;top:970px">$200/Weekend*</div>
    <div class="rate-capacity" style="top:1003px"><b>Capacity:</b> 10,000 lb GVWR · 20' x 7' tilt deck</div>
  </section>

  <div class="trailer-label" style="top:783px">RL 20' X 7' CAR HAULER</div>
  <div class="trailer-label" style="top:973px">RL 20' X 7' CAR HAULER</div>

  <h2 class="service-title">AREA OF SERVICE</h2>
  <div class="service-list">
    <span>WAYNE. MI</span><span>LAPEER. MI</span>
    <span>GENESEE. MI</span><span>ST. CLAIR. MI</span>
    <span>MONROE. MI</span><span>LIVINGSTON. MI</span>
    <span>WASHTENAW. MI</span><span></span>
  </div>

  <div class="website">kandmtrailer-example.com</div>
  <div class="phone-number">(248)555-0186</div>
</main>
</body>
</html>
```